Need a professional card design. Marlowe building company specialise in residential and commercial builds. New homes, additions & renovations.
Wanting a card with creativity and professionalism.
Want card that utilises logo.

Back and front.

I have just created a logo, and want to use it on the business card.
Attached a copy of the logo.
Attached is also a current business card which I wish to redesign

please utilise both sides

• Reg# 38095

```html
<!DOCTYPE html>
<html lang="en">
<head>
<meta charset="utf-8">
<title>Marlowe Building Co – Business Card</title>
<link rel="stylesheet" href="https://fonts.googleapis.com/css2?family=Montserrat:wght@400;600;700&family=Libre+Baskerville:wght@400;700&display=swap">
<style>
  :root {
    --page-bg: #e9e6e1;
    --dark-top: #33271f;
    --dark-bottom: #181210;
    --gold: #eba232;
    --white: #ffffff;
    --ink: #1d1d1d;
    --muted: #9a9a9a;
    --rule: #cfcfcf;
  }
  * { box-sizing: border-box; margin: 0; padding: 0; }
  html, body { width: 1200px; height: 1024px; overflow: hidden; }
  body {
    background: var(--page-bg);
    display: flex;
    flex-direction: column;
    align-items: center;
    justify-content: center;
    gap: 40px;
    font-family: "Montserrat", sans-serif;
  }
  .card {
    width: 800px;
    height: 457px;
    position: relative;
    box-shadow: 0 6px 18px rgba(0,0,0,0.18);
  }

  /* Front */
  .card-front {
    background: radial-gradient(ellipse at 40% 35%, var(--dark-top), var(--dark-bottom) 80%);
    display: flex;
    flex-direction: column;
    align-items: center;
    padding-top: 120px;
  }
  .brand {
    display: flex;
    align-items: center;
    gap: 14px;
  }
  .brand-dot {
    border-radius: 50%;
    background: var(--gold);
    flex: none;
  }
  .brand-name {
    font-family: "Montserrat", sans-serif;
    font-weight: 600;
    color: var(--gold);
    letter-spacing: 0.06em;
    line-height: 1;
    text-transform: uppercase;
  }
  .card-front .brand-dot { width: 30px; height: 30px; }
  .card-front .brand-name { font-size: 44px; }
  .tagline {
    font-family: "Libre Baskerville", serif;
    color: var(--gold);
    text-align: center;
    line-height: 1.35;
  }
  .card-front .tagline {
    margin-top: 56px;
    font-size: 22px;
  }
  .front-rule {
    position: absolute;
    left: 120px;
    right: 120px;
    bottom: 70px;
    height: 1.5px;
    background: var(--gold);
  }

  /* Back */
  .card-back {
    background: var(--white);
    overflow: hidden;
  }
  .back-band {
    position: absolute;
    left: 0; right: 0; bottom: 0;
    height: 22px;
    background: var(--gold);
  }
  .back-top {
    position: absolute;
    left: 56px; right: 56px; top: 48px;
    display: flex;
    justify-content: space-between;
    align-items: flex-start;
  }
  .card-back .brand-dot { width: 18px; height: 18px; }
  .card-back .brand-name { font-size: 26px; }
  .card-back .tagline {
    font-size: 15px;
    color: var(--ink);
    text-align: right;
  }
  .person {
    position: absolute;
    left: 56px; top: 170px;
  }
  .person-name {
    font-family: "Libre Baskerville", serif;
    font-weight: 700;
    font-variant: small-caps;
    font-size: 30px;
    color: var(--ink);
    letter-spacing: 0.02em;
  }
  .person-role {
    margin-top: 8px;
    font-weight: 700;
    font-size: 15px;
    color: var(--gold);
  }
  .back-rule {
    position: absolute;
    left: 56px; right: 56px; top: 282px;
    height: 1px;
    background: var(--rule);
  }
  .contacts {
    position: absolute;
    left: 56px; top: 304px;
    list-style: none;
    display: flex;
    flex-direction: column;
    gap: 9px;
  }
  .contacts li {
    display: flex;
    align-items: center;
    gap: 14px;
    font-size: 16px;
    color: var(--ink);
  }
  .contacts svg { width: 16px; height: 16px; flex: none; }
  .reg-no {
    position: absolute;
    right: 56px; bottom: 46px;
    font-weight: 700;
    font-size: 15px;
    color: var(--ink);
  }
</style>
</head>
<body>

  <section class="card card-front" aria-label="Card front">
    <div class="brand">
      <span class="brand-dot"></span>
      <span class="brand-name">Marlowe Building Co</span>
    </div>
    <p class="tagline">New Homes - Additions &amp; Renovations<br>Domestic &amp; Commercial Builders</p>
    <div class="front-rule"></div>
  </section>

  <section class="card card-back" aria-label="Card back">
    <div class="back-top">
      <div class="brand">
        <span class="brand-dot"></span>
        <span class="brand-name">Marlowe Building Co</span>
      </div>
      <p class="tagline">New Homes - Additions &amp; Renovations<br>Domestic &amp; Commercial Builders</p>
    </div>

    <div class="person">
      <p class="person-name">Daniel Hartley</p>
      <p class="person-role">Director</p>
    </div>

    <div class="back-rule"></div>

    <ul class="contacts">
      <li>
        <svg viewBox="0 0 16 16" aria-hidden="true"><path d="M4 1.5 6.5 4 5 6c.8 1.9 2.2 3.3 4 4.2l2-1.5 2.5 2.5-1.6 2.3C7 13 3 9 1.8 3.1Z" fill="var(--gold)"/></svg>
        <span>08 9412 6630</span>
      </li>
      <li>
        <svg viewBox="0 0 16 16" aria-hidden="true"><rect x="2" y="5" width="12" height="8" rx="1.5" fill="var(--gold)"/><rect x="4.5" y="2" width="7" height="4" fill="none" stroke="var(--gold)" stroke-width="1.4"/></svg>
        <span>08 9412 6631</span>
      </li>
      <li>
        <svg viewBox="0 0 16 16" aria-hidden="true"><rect x="4" y="1" width="8" height="14" rx="1.5" fill="none" stroke="var(--gold)" stroke-width="1.6"/><circle cx="8" cy="12.3" r="0.9" fill="var(--gold)"/></svg>
        <span>0412 558 190</span>
      </li>
      <li>
        <svg viewBox="0 0 16 16" aria-hidden="true"><rect x="1.5" y="3.5" width="13" height="9" rx="1" fill="var(--gold)"/><path d="M2 4.5 8 9l6-4.5" fill="none" stroke="var(--white)" stroke-width="1.2"/></svg>
        <span>marlowebuildingco@mailbox.com</span>
      </li>
    </ul>

    <p class="reg-no">Reg. No. 38095</p>
    <div class="back-band"></div>
  </section>

</body>
</html>
```